Corvane Lending Partners - Real estate loans - need a business card with a logo

I need a logo and a business card that looks elegant - that looks as if it is a big stablish corporation - We do real estate loans, my goal is to brand myself with colors black background - gold or silver letters - some combination - Name of the company different color than the rest of the card -

```html
<!DOCTYPE html>
<html lang="en">
<head>
<meta charset="utf-8">
<title>Corvane Lending Partners – Business Card</title>
<link rel="stylesheet" href="https://fonts.googleapis.com/css2?family=Montserrat:wght@400;500;600;700&display=swap">
<style>
  :root {
    --backdrop: #d9d7d1;
    --card: #0b0b0b;
    --gold: #c9a545;
    --silver: #d6d6d6;
  }
  * { margin: 0; padding: 0; box-sizing: border-box; }
  html, body {
    width: 1200px; height: 884px; overflow: hidden;
    background: var(--backdrop);
    font-family: "Montserrat", sans-serif;
  }
  .canvas { position: relative; width: 1200px; height: 884px; }
  .card {
    position: absolute; width: 540px; height: 310px;
    background: var(--card);
    border-radius: 3px;
    box-shadow: 0 6px 14px rgba(0,0,0,0.25);
  }
  .card-front { left: 70px; top: 120px; }
  .card-back { left: 600px; top: 440px; }

  .brand-name {
    color: var(--gold); font-weight: 600; letter-spacing: 2px;
    text-transform: uppercase; font-size: 17px; line-height: 1.2;
    white-space: nowrap;
  }
  .card-front .brand-name {
    position: absolute; left: 0; right: 0; top: 50%;
    transform: translateY(-50%); text-align: center;
  }
  .card-back .brand-name {
    position: absolute; right: 44px; top: 62px; font-size: 14px;
  }

  .address {
    position: absolute; right: 44px; top: 150px; text-align: right;
    color: var(--silver); font-size: 12px; line-height: 1.55;
  }
  .holder { position: absolute; left: 40px; bottom: 36px; }
  .holder-name {
    color: var(--gold); font-weight: 700; font-size: 15px; letter-spacing: 0.5px;
    text-transform: uppercase;
  }
  .holder-title { color: var(--silver); font-size: 12px; margin-top: 2px; }
  .divider { width: 22px; height: 2px; background: var(--gold); margin: 12px 0 10px; }
  .contact { list-style: none; }
  .contact li {
    display: flex; align-items: center; gap: 8px;
    color: var(--silver); font-size: 11.5px; line-height: 1.75;
  }
  .contact svg { width: 12px; height: 12px; flex: none; }
</style>
</head>
<body>
<main class="canvas">
  <section class="card card-front" aria-label="Card front">
    <p class="brand-name">Corvane Lending Partners</p>
  </section>

  <section class="card card-back" aria-label="Card back">
    <p class="brand-name">Corvane Lending Partners</p>
    <p class="address">48 Harbour Crest Lane,<br>Markham, ON L3R 5K2</p>

    <div class="holder">
      <p class="holder-name">Marcus Ellery</p>
      <p class="holder-title">Managing Director</p>
      <div class="divider"></div>
      <ul class="contact">
        <li>
          <svg viewBox="0 0 12 12" aria-hidden="true"><path fill="var(--gold)" d="M2.5 1h2l1 2.5-1.3 1a6 6 0 0 0 3.3 3.3l1-1.3L11 7.5v2c0 .8-.7 1.5-1.5 1.5A8.5 8.5 0 0 1 1 2.5C1 1.7 1.7 1 2.5 1z"/></svg>
          +1 905 555 0148
        </li>
        <li>
          <svg viewBox="0 0 12 12" aria-hidden="true"><rect x="0.5" y="2" width="11" height="8" fill="var(--gold)"/><path d="M1 2.5l5 4 5-4" stroke="var(--card)" stroke-width="1" fill="none"/></svg>
          mellery@corvane.com
        </li>
        <li>
          <svg viewBox="0 0 12 12" aria-hidden="true"><circle cx="6" cy="6" r="5" fill="none" stroke="var(--gold)" stroke-width="1.2"/><ellipse cx="6" cy="6" rx="2" ry="5" fill="none" stroke="var(--gold)" stroke-width="1"/><path d="M1 6h10" stroke="var(--gold)" stroke-width="1"/></svg>
          www.corvanelending.com
        </li>
      </ul>
    </div>
  </section>
</main>
</body>
</html>
```